Redesign der Systemmails von formwerkstatt.de
Zielgruppe
Wir sind die Macher von formwerkstatt.de und wollen unsere Standardmails, die systemseitig verschickt werden, schöner und wertiger gestalten.
Aufgabenstellung
Wir sind der Meinung, dass unsere System-E-Mails ein Redesign nötig haben. Daher würden wir Dich bitten, uns Deinen Input zu geben. Die Mails sollen schlichter und moderner gestaltet werden. Folgende Elemente bedürfen aus unserer Sicht der Überarbeitung:
Schrift -> Aktuell verwenden wir Lucida Sans Unicode als Schrift für die Mails. Die Schrift passt aber nicht mehr so gut zur Seite. Auf der Seite verwenden wir inzwischen die Lato (leider keine Systemschrift).
Bitte schlage eine aus Deiner Sicht geeignete Systemschrift vor.
Buttonstyle -> Bitte einen frischen Buttonstyle vorschlagen
Schriftgröße und Farbe der Headline, des Fließtextes und des Footers -> Bitte harmonische Einteilung finden
Einen Screenshot einer aktuellen Mail ist anbei, außerdem einige Beispiele gelungener Mails anderer Unternehmen.
Die Datenlieferung sollte dann bitte als PSD und einer textlichen Beschreibung der Schriften, Schriftgrößen und Farbwerte erfolgen.
Bitte folgenden Text für die Gestaltung verwenden:
Hallo VORNAME NACHNAME,
Ihr Projekt 'BEISPIELPROJEKTTITEL' ist abgelaufen. Als nächstes sollten Sie ein Gewinner-Design bestimmen:
Button [Gewinner bestimmen]
Sie möchten noch Feinheiten am Design ändern lassen? Kein Problem: Finale Änderungen am Gewinnerdesign erledigt der Designer gerne im Rahmen der Datenübergabe. Küren Sie einfach Ihren Favoriten zum Gewinner und teilen Sie dem Designer Ihre Änderungswünsche in der Datenübergabe mit. Erst wenn Sie bestätigt haben, dass alle Daten mit den gewünschten Überarbeitungen vollständig übergeben wurden, wird das Preisgeld an den Designer transferiert.
Sie können sich zwischen Ihren Favoriten nicht entscheiden?
Kein Problem, nutzen Sie einfach unser praktisches Design-Voting und lassen Sie Familie, Freunde, Bekannte und Kollegen abstimmen. So sehen Sie, welches Design am besten ank..

```html
<!DOCTYPE html>
<html lang="de">
<head>
<meta charset="utf-8">
<title>formwerkstatt.de – Projekt abgelaufen</title>
<link href="https://fonts.googleapis.com/css2?family=Roboto:wght@400;500;700&display=swap" rel="stylesheet">
<style>
  :root {
    --page-bg: #ffffff;
    --sheet-bg: #e8f6fd;
    --header-start: #0f9fe2;
    --header-mid: #3ab9f0;
    --header-end: #0b9be0;
    --accent: #0898dc;
    --text: #555a5e;
    --text-strong: #3f4448;
    --card: #ffffff;
    --info-card: #fbfbfa;
    --icon-tile: #f5f5f5;
    --trophy: #f4b400;
    --footer-text: #7a8085;
  }
  * { box-sizing: border-box; margin: 0; padding: 0; }
  html, body { width: 863px; height: 1200px; overflow: hidden; }
  body {
    background: var(--page-bg);
    font-family: "Roboto", Arial, sans-serif;
    color: var(--text);
    position: relative;
  }
  .mail {
    position: absolute;
    left: 60px; top: 80px;
    width: 742px; height: 1040px;
    background: var(--sheet-bg);
    box-shadow: 0 3px 10px rgba(0,0,0,0.35);
    overflow: hidden;
  }
  .mail-header {
    position: absolute; left: 0; top: 0;
    width: 100%; height: 226px;
    background: linear-gradient(90deg, var(--header-start) 0%, var(--header-mid) 50%, var(--header-end) 100%);
  }
  .brand {
    position: absolute; top: 58px; left: 0; width: 100%;
    display: flex; justify-content: center; align-items: center; gap: 12px;
    color: #fff; font-size: 27px; font-weight: 500; letter-spacing: 0.2px;
  }
  .brand-mark { width: 22px; height: 22px; background: #fff; border-radius: 3px; }
  .content-card {
    position: absolute; left: 98px; top: 137px;
    width: 548px; height: 657px;
    background: var(--card);
    border-radius: 5px;
    padding: 0 56px;
  }
  .greeting {
    text-align: center; font-size: 21px; font-weight: 400;
    color: var(--text-strong); margin-top: 38px; line-height: 26px;
  }
  .greeting strong { color: var(--accent); font-weight: 700; }
  .intro {
    margin-top: 52px; font-size: 15px; line-height: 22px; letter-spacing: 0.2px;
  }
  .intro strong { color: var(--accent); font-weight: 700; }
  .cta {
    display: flex; margin: 28px 0 0 56px;
    width: 325px; height: 62px; border-radius: 4px; overflow: hidden;
    box-shadow: 0 2px 5px rgba(0,0,0,0.25);
    text-decoration: none;
  }
  .cta-icon {
    width: 59px; background: var(--icon-tile);
    display: flex; align-items: center; justify-content: center;
  }
  .cta-label {
    flex: 1; background: var(--accent); color: #fff;
    font-size: 15px; font-weight: 700; letter-spacing: 1.1px;
    display: flex; align-items: center; justify-content: center;
    position: relative;
  }
  .cta-label::before {
    content: ""; position: absolute; left: 0; top: 50%;
    transform: translateY(-50%);
    border-left: 9px solid var(--icon-tile);
    border-top: 9px solid transparent; border-bottom: 9px solid transparent;
  }
  .body-copy { margin-top: 56px; }
  .body-copy p {
    font-size: 15px; line-height: 22px; letter-spacing: 0.2px;
    text-align: justify; margin-bottom: 22px;
  }
  .help-card {
    position: absolute; left: 98px; top: 804px;
    width: 548px; height: 132px;
    background: var(--info-card); border-radius: 5px;
    padding: 26px 24px 0 24px;
  }
  .help-title {
    text-align: center; color: var(--accent);
    font-size: 17px; font-weight: 700; line-height: 22px;
  }
  .help-text { margin-top: 20px; font-size: 15px; line-height: 22px; }
  .help-text strong { color: var(--text-strong); font-weight: 700; }
  .legal {
    position: absolute; left: 54px; top: 959px; width: 660px;
    font-size: 7.6px; line-height: 14px; color: var(--footer-text);
    white-space: nowrap;
  }
</style>
</head>
<body>
  <main class="mail">
    <header class="mail-header">
      <div class="brand"><span class="brand-mark"></span><span>formwerkstatt.de</span></div>
    </header>

    <section class="content-card">
      <h1 class="greeting">Hallo <strong>Vorname Nachname</strong>,</h1>
      <p class="intro">Ihr Projekt <strong>'BEISPIELPROJEKTTITEL'</strong> ist abgelaufen.<br>Als nächstes sollten Sie ein Gewinner-Design bestimmen:</p>

      <a class="cta" href="#">
        <span class="cta-icon">
          <svg width="24" height="24" viewBox="0 0 24 24" aria-hidden="true">
            <path d="M6 3h12v4a6 6 0 0 1-12 0z" fill="var(--trophy)"/>
            <path d="M6 5H3v2a4 4 0 0 0 4 4M18 5h3v2a4 4 0 0 1-4 4" fill="none" stroke="var(--trophy)" stroke-width="1.8"/>
            <rect x="10.5" y="12.5" width="3" height="5" fill="var(--trophy)"/>
            <rect x="7" y="17.5" width="10" height="3" rx="1" fill="var(--trophy)"/>
            <circle cx="12" cy="7" r="1.6" fill="#fff"/>
          </svg>
        </span>
        <span class="cta-label">GEWINNER BESTIMMEN</span>
      </a>

      <div class="body-copy">
        <p>Sie möchten noch Feinheiten am Design ändern lassen? Kein Problem: Finale Änderungen am Gewinnerdesign erledigt der Designer gerne im Rahmen der Datenübergabe.</p>
        <p>Küren Sie einfach Ihren Favoriten zum Gewinner und teilen Sie dem Designer Ihre Änderungswünsche in der Datenübergabe mit. Erst wenn Sie bestätigt haben, dass alle Daten mit den gewünschten Überarbeitungen vollständig übergeben wurden, wird das Preisgeld an den Designer transferiert.</p>
        <p>Sie können sich zwischen Ihren Favoriten nicht entscheiden? Kein Problem, nutzen Sie einfach unser praktisches Design-Voting und lassen Sie Familie, Freunde, Bekannte und Kollegen abstimmen. So sehen Sie, welches Design am besten ankommt.</p>
      </div>
    </section>

    <section class="help-card">
      <h2 class="help-title">Haben Sie noch Fragen?</h2>
      <p class="help-text">Schreiben Sie uns einfach eine Mail unter <strong>support@formwerkstatt.de</strong><br>oder rufen Sie uns an: <strong>0911-48207315</strong></p>
    </section>

    <footer class="legal">
      formwerkstatt.de GmbH, Mühlweg 7, 90402 Nürnberg, Deutschland, Geschäftsführer: Jonas Reiter und Lena Hofbauer, Amtsgericht Nürnberg: HRB 31577<br>
      Sie können Ihre Maileinstellungen jederzeit ändern, indem Sie hier klicken: https://www.formwerkstatt.de/account.php?page=details.
    </footer>
  </main>
</body>
</html>
```